Our architectural studio needs a new business card

We need a business card design for our studio based in Waterloo in Belgium. We are active in architecture, design and installation.
Our works are contemporary and minimalist. our clients are refined and cultured.
Our business card must be minimalist and refined.

Reason: Some designers have accepted my invitation but they don't have all replied. I want to give them a chance to make one proposal. Paul

Target Market(s)

architecture

Industry/Entity Type

Business

Contact Information for Business Card

studio: paul dorsande studio
paul dorsande, architecte
M. +32 471 982 615
F. +322 618 4097
www.pauldorsande-example.com
paul@pauldorsande-example.com
14 rue des Margelles
1410 Waterloo
Belgium

Font styles to use
Sans Serif

Requirements
Must have
• simple, minimalist, clear, elegant and chic! Black and white
Nice to have
• embossed logo, other format like a square for example
Should not have
• color, fantasy, curves, ...

```html
<!DOCTYPE html>
<html lang="fr">
<head>
<meta charset="utf-8">
<title>Paul Dorsande Studio — Business Card</title>
<link rel="stylesheet" href="https://fonts.googleapis.com/css2?family=Montserrat:wght@500;600;700&family=Arimo:wght@400&display=swap">
<style>
  :root {
    --backdrop: #a9a9a9;
    --card-black: #141414;
    --blade-black: #050505;
    --edge-silver: #8a8a8a;
    --text-silver: #cfcfcf;
    --paper-white: #ffffff;
    --paper-shade: #dcdcdc;
    --ink-black: #0a0a0a;
  }
  * { margin: 0; padding: 0; box-sizing: border-box; }
  html, body { width: 1200px; height: 800px; overflow: hidden; }
  body {
    background: var(--backdrop);
    display: flex;
    align-items: center;
    justify-content: center;
    gap: 40px;
  }
  .card {
    position: relative;
    width: 540px;
    height: 309px;
    border-radius: 16px;
    overflow: hidden;
  }
  .card svg.card-art { position: absolute; inset: 0; width: 100%; height: 100%; }

  /* Front */
  .card-front { background: var(--card-black); color: var(--text-silver); }
  .front-brand {
    position: absolute;
    left: 40px; top: 0; width: 214px; height: 100%;
    display: flex; flex-direction: column; align-items: center; justify-content: center; gap: 16px;
  }
  .brand-square { width: 34px; height: 34px; background: var(--text-silver); }
  .brand-name {
    font-family: "Montserrat", sans-serif; font-weight: 600;
    font-size: 10px; letter-spacing: 2.5px; text-transform: uppercase;
    text-align: center; white-space: nowrap;
  }
  .front-divider {
    position: absolute; left: 268px; top: 56px; width: 1px; height: 150px;
    background: var(--edge-silver);
  }
  .front-contact {
    position: absolute; left: 300px; top: 40px; right: 20px;
  }
  .person-name {
    font-family: "Montserrat", sans-serif; font-weight: 700;
    font-size: 19px; letter-spacing: 3px; text-transform: uppercase;
  }
  .person-role {
    font-family: "Arimo", sans-serif; font-size: 15px; letter-spacing: 1px;
    text-align: right; margin: 2px 12px 16px 0;
  }
  .contact-list { list-style: none; font-family: "Arimo", sans-serif; font-size: 13px; line-height: 20px; }
  .contact-list li { display: flex; align-items: center; gap: 8px; white-space: nowrap; }
  .contact-list svg { width: 12px; height: 12px; flex: none; }
  .contact-list .no-icon { padding-left: 20px; }

  /* Back */
  .card-back {
    background: radial-gradient(ellipse at center, var(--paper-white) 35%, var(--paper-shade) 100%);
  }
  .back-brand {
    position: absolute; left: 50%; top: 50%; transform: translate(-50%, -50%);
    display: flex; flex-direction: column; align-items: center; gap: 14px;
    color: var(--ink-black);
  }
  .back-brand .brand-square { background: var(--ink-black); }
</style>
</head>
<body>

  <section class="card card-front" aria-label="Card front">
    <svg class="card-art" viewBox="0 0 540 309" aria-hidden="true">
      <polygon points="0,0 170,0 0,85" fill="var(--blade-black)" stroke="var(--edge-silver)" stroke-width="2"/>
      <polygon points="0,220 0,309 140,309" fill="var(--blade-black)" stroke="var(--edge-silver)" stroke-width="2"/>
    </svg>

    <div class="front-brand">
      <div class="brand-square"></div>
      <p class="brand-name">Paul Dorsande Studio</p>
    </div>

    <div class="front-divider"></div>

    <div class="front-contact">
      <p class="person-name">Paul Dorsande</p>
      <p class="person-role">Architecte</p>
      <ul class="contact-list">
        <li>
          <svg viewBox="0 0 12 12"><rect x="3" y="0.5" width="6" height="11" rx="1" fill="none" stroke="currentColor"/></svg>
          +32 471 982 615
        </li>
        <li>
          <svg viewBox="0 0 12 12"><rect x="1" y="4" width="10" height="7" fill="none" stroke="currentColor"/><rect x="3" y="1" width="6" height="3" fill="none" stroke="currentColor"/></svg>
          +322 618 4097
        </li>
        <li>
          <svg viewBox="0 0 12 12"><circle cx="6" cy="6" r="5" fill="none" stroke="currentColor"/><path d="M1 6h10M6 1c-3 3-3 7 0 10M6 1c3 3 3 7 0 10" fill="none" stroke="currentColor" stroke-width="0.8"/></svg>
          www.pauldorsande-example.com
        </li>
        <li>
          <svg viewBox="0 0 12 12"><rect x="0.5" y="2.5" width="11" height="7" fill="none" stroke="currentColor"/><path d="M0.5 2.5 6 7l5.5-4.5" fill="none" stroke="currentColor"/></svg>
          paul@pauldorsande-example.com
        </li>
        <li>
          <svg viewBox="0 0 12 12"><path d="M6 11.5 2.5 6a3.5 3.5 0 1 1 7 0Z" fill="currentColor"/><circle cx="6" cy="4.5" r="1.3" fill="var(--card-black)"/></svg>
          14 rue des Margelles
        </li>
        <li class="no-icon">1395 Valmerelle Ostrand</li>
      </ul>
    </div>
  </section>

  <section class="card card-back" aria-label="Card back">
    <svg class="card-art" viewBox="0 0 540 309" aria-hidden="true">
      <polygon points="0,0 360,0 305,62 0,62" fill="var(--blade-black)"/>
      <polygon points="405,0 540,0 540,215 468,215 468,72" fill="var(--blade-black)"/>
      <polygon points="175,309 540,309 540,250 225,250" fill="var(--blade-black)"/>
      <polygon points="0,95 72,95 72,240 118,309 0,309" fill="var(--blade-black)"/>
    </svg>
    <div class="back-brand">
      <div class="brand-square"></div>
      <p class="brand-name">Paul Dorsande Studio</p>
    </div>
  </section>

</body>
</html>
```